The Lantern Circle

I need a design for a 1 page flyer but also a brochure

Target Market(s)

Wealthy, elegant, intelligent, discerning women who are on a journey of self-discovery.

Industry/Entity Type

Spiritual and personal development, yoga, meditation

Requirements
Must have
• Be very elegant, attractive, upmarket minimalist but also bit mystical
Nice to have
• I would like to use my logo (see uploaded file). The texts are also uploaded. One for the 1 page flyer 1 for a full brochure
Should not have
• be too busy, multicoloured, garish.

```html
<!DOCTYPE html>
<html lang="en">
<head>
<meta charset="utf-8">
<title>The Lantern Circle – Flyer</title>
<link href="https://fonts.googleapis.com/css2?family=Alegreya+Sans:wght@300;400;500;700&family=Lora:ital,wght@0,400;0,700;1,400;1,500&display=swap" rel="stylesheet">
<style>
  :root{
    --canvas:#7a7574;
    --forest:#0f4d2a;
    --forest-deep:#0b3f22;
    --leaf:#1c6b37;
    --ink:#203a4c;
    --gold:#9d8a62;
    --sand:#a89a7c;
    --white:#ffffff;
    --mist:#eceeec;
    --soft-grey:#7f8a85;
  }
  *{box-sizing:border-box;margin:0;padding:0}
  html,body{width:1200px;height:769px;overflow:hidden}
  body{background:var(--canvas);font-family:"Alegreya Sans",sans-serif;position:relative}
  .page{position:absolute;top:41px;width:531px;height:683px;overflow:hidden}
  .page--front{left:48px;background:var(--white)}
  .page--back{left:600px;background:var(--white)}
  .abs{position:absolute}
  svg.layer{position:absolute;left:0;top:0}

  /* front */
  .title{left:37px;top:34px;color:var(--forest);font-weight:400;font-size:46px;line-height:46px;letter-spacing:.5px}
  .subtitle{left:36px;top:142px;color:var(--ink);font-size:17.5px;font-weight:400;letter-spacing:.2px}
  .place{left:36px;top:163px;color:var(--ink);font-size:14px}
  .lede{left:36px;top:201px;width:230px;color:var(--forest);font-size:14.5px;line-height:18.5px}
  .setting{left:36px;top:264px;width:180px;color:#2a2a2a;font-size:9.5px;line-height:13px}

  .heading-white{color:var(--white);font-weight:700}
  .exp-title{left:37px;top:398px;font-size:19px;line-height:25px}
  .ticks{list-style:none;color:var(--white)}
  .ticks li{display:flex;align-items:center;gap:5px}
  .ticks svg{flex:none}
  .ticks--front{left:36px;top:454px;font-size:11px;line-height:15.2px}
  .why-title{left:287px;top:462px;font-size:17px;line-height:22px}
  .why-text{left:287px;top:511px;width:220px;color:var(--white);font-size:9px;line-height:12.2px}

  .name-mark{color:var(--white);font-weight:300;text-align:center;letter-spacing:.3px}
  .name-mark--front{left:22px;top:632px;width:80px;font-size:9px;line-height:10.5px}
  .name-mark--front .dot{display:block;width:22px;height:22px;border-radius:50%;background:var(--white);margin:0 auto 6px}
  .loc-title{left:111px;top:590px;font-size:14px}
  .loc-line{left:111px;top:610px;width:434px;display:flex;align-items:center;gap:4px;color:var(--gold);font-size:7.5px;font-weight:700}
  .loc-line i{flex:1;border-bottom:1px dotted var(--gold);height:0}
  .quote-mark{left:109px;top:660px;color:var(--white);font-family:Lora,serif;font-size:22px;line-height:20px}
  .loc-quote{left:134px;top:627px;width:214px;color:var(--white);font-size:7.7px;line-height:10px;border-left:1px solid rgba(255,255,255,.6);padding-left:7px}
  .loc-quote small{display:block;font-size:6.3px;margin-top:2px}
  .vdots{border-left:1px dotted var(--gold)}
  .contact--front{left:368px;top:625px;color:var(--white)}
  .phone{font-family:Lora,serif;font-weight:700}
  .contact--front .phone{font-size:13px;line-height:16px}
  .contact--front .web{font-family:Lora,serif;font-size:8px;line-height:10.5px}

  /* back */
  .exp-title--back{left:306px;top:49px;font-size:18.5px;line-height:25px}
  .ticks--back{left:306px;top:102px;font-size:10.8px;line-height:17.7px}
  .name-mark--back{left:368px;top:426px;width:200px;color:var(--soft-grey);font-size:17px;line-height:20px;font-weight:300;text-align:center}
  .name-mark--back .dot{display:block;width:46px;height:46px;border-radius:50%;background:var(--forest);margin:0 auto 14px}
  .sec-title{color:var(--forest);font-weight:700;font-size:20px}
  .sec-text{color:#444;font-size:11.5px;line-height:15.5px}
  .pricing{left:36px;top:500px;width:200px}
  .reserve{left:272px;top:500px;width:230px}
  .reserve .sec-text{font-size:10.8px;line-height:14.5px}
  .rule{left:36px;top:582px;width:473px;border-top:1px solid var(--sand)}
  .contact--back{left:36px;top:598px;color:#333}
  .contact--back .phone{font-size:17.5px;line-height:22px;color:#2c2c2c}
  .contact--back .web{font-family:Lora,serif;font-size:10.8px;line-height:14px}
  .quote-badge{left:232px;top:611px;width:26px;height:26px;border-radius:50%;background:var(--gold);color:var(--white);font-family:Lora,serif;font-weight:700;font-size:16px;line-height:31px;text-align:center}
  .closing{left:271px;top:599px;color:var(--forest);font-family:Lora,serif;font-style:italic;font-size:18px;line-height:23px}
</style>
</head>
<body>

<!-- Front -->
<section class="page page--front">
  <svg class="layer" width="531" height="683" viewBox="0 0 531 683">
    <defs>
      <linearGradient id="villaFade" x1="0" y1="0" x2="1" y2="1">
        <stop offset="0" stop-color="#d9d6ce"/>
        <stop offset=".5" stop-color="#eeece7"/>
        <stop offset="1" stop-color="#ffffff"/>
      </linearGradient>
      <linearGradient id="dusk" x1="0" y1="0" x2="0" y2="1">
        <stop offset="0" stop-color="#4a4f5e"/>
        <stop offset=".45" stop-color="#8d6a68"/>
        <stop offset=".68" stop-color="#d07a3a"/>
        <stop offset="1" stop-color="#3a1a12"/>
      </linearGradient>
    </defs>
    <rect width="531" height="380" fill="url(#villaFade)" opacity=".55" role="img" aria-label="Faded photo of a stone Tuscan villa with a pool"/>
    <path d="M0 360 C80 345 170 330 260 395 C320 438 400 450 460 420 C495 400 515 380 531 360 L531 683 L0 683Z" fill="var(--leaf)"/>
    <path d="M0 380 C80 360 170 350 260 412 C330 460 420 470 531 410 L531 683 L0 683Z" fill="var(--forest)"/>
    <circle cx="412" cy="305" r="135" fill="var(--white)"/>
    <circle cx="412" cy="300" r="126" fill="url(#dusk)" role="img" aria-label="Photo of a person meditating in silhouette against a sunset sky"/>
  </svg>

  <h1 class="abs title">THE LANTERN<br>CIRCLE</h1>
  <p class="abs subtitle">PATHWAYS TO OUR TRUE ESSENCE</p>
  <p class="abs place">TUSCANY, ITALY</p>
  <p class="abs lede">A refined, intimate journey into inner quiet, energetic awakening, and embodied presence</p>
  <p class="abs setting">held within the beauty and serenity of a private Tuscan villa</p>

  <h2 class="abs heading-white exp-title">What You Will<br>Experience</h2>
  <ul class="abs ticks ticks--front">
    <li><svg width="9" height="9" viewBox="0 0 10 10"><circle cx="5" cy="5" r="4.3" fill="none" stroke="currentColor" stroke-width=".9"/><path d="M3 5.1l1.4 1.4L7 3.8" fill="none" stroke="currentColor" stroke-width=".9"/></svg>Energetic activation &amp; exploration</li>
    <li><svg width="9" height="9" viewBox="0 0 10 10"><circle cx="5" cy="5" r="4.3" fill="none" stroke="currentColor" stroke-width=".9"/><path d="M3 5.1l1.4 1.4L7 3.8" fill="none" stroke="currentColor" stroke-width=".9"/></svg>Meditation &amp; breathwork</li>
    <li><svg width="9" height="9" viewBox="0 0 10 10"><circle cx="5" cy="5" r="4.3" fill="none" stroke="currentColor" stroke-width=".9"/><path d="M3 5.1l1.4 1.4L7 3.8" fill="none" stroke="currentColor" stroke-width=".9"/></svg>Somatic movement &amp; intuitive embodiment</li>
    <li><svg width="9" height="9" viewBox="0 0 10 10"><circle cx="5" cy="5" r="4.3" fill="none" stroke="currentColor" stroke-width=".9"/><path d="M3 5.1l1.4 1.4L7 3.8" fill="none" stroke="currentColor" stroke-width=".9"/></svg>Shadow exploration</li>
    <li><svg width="9" height="9" viewBox="0 0 10 10"><circle cx="5" cy="5" r="4.3" fill="none" stroke="currentColor" stroke-width=".9"/><path d="M3 5.1l1.4 1.4L7 3.8" fill="none" stroke="currentColor" stroke-width=".9"/></svg>Sound &amp; frequency immersion</li>
    <li><svg width="9" height="9" viewBox="0 0 10 10"><circle cx="5" cy="5" r="4.3" fill="none" stroke="currentColor" stroke-width=".9"/><path d="M3 5.1l1.4 1.4L7 3.8" fill="none" stroke="currentColor" stroke-width=".9"/></svg>Reiki healing</li>
    <li><svg width="9" height="9" viewBox="0 0 10 10"><circle cx="5" cy="5" r="4.3" fill="none" stroke="currentColor" stroke-width=".9"/><path d="M3 5.1l1.4 1.4L7 3.8" fill="none" stroke="currentColor" stroke-width=".9"/></svg>Forest bathing</li>
    <li><svg width="9" height="9" viewBox="0 0 10 10"><circle cx="5" cy="5" r="4.3" fill="none" stroke="currentColor" stroke-width=".9"/><path d="M3 5.1l1.4 1.4L7 3.8" fill="none" stroke="currentColor" stroke-width=".9"/></svg>Craftwork to soothe the nervous system</li>
  </ul>

  <h2 class="abs heading-white why-title">Why This Retreat<br>Is Different</h2>
  <p class="abs why-text">This is not a yoga retreat — though yoga informs the work. It is a deeply personalised, spacious, and elegant invitation to return to your essence. With only 5–8 participants, each guest receives individualised attention, intuitive guidance, and profound holding</p>

  <div class="abs name-mark name-mark--front"><span class="dot"></span>THE LANTERN<br>CIRCLE</div>
  <h3 class="abs heading-white loc-title">Location</h3>
  <div class="abs loc-line"><span>Villa Castagneto, Tuscany</span><i></i></div>
  <span class="abs quote-mark">“</span>
  <p class="abs loc-quote">A serene historic villa surrounded by rolling hills, ancient trees, and luminous Tuscan light<small>— an ideal setting for restoration and inner exploration.</small></p>
  <div class="abs vdots" style="left:354px;top:628px;height:40px"></div>
  <div class="abs contact--front">
    <p class="phone">+41 79 555 01 28</p>
    <p class="web">hello@lanterncircle-retreats.com</p>
    <p class="web">www.LanternCircle-Retreats.com</p>
  </div>
</section>

<!-- Back -->
<section class="page page--back">
  <svg class="layer" width="531" height="683" viewBox="0 0 531 683">
    <defs>
      <linearGradient id="hills" x1="0" y1="0" x2="0" y2="1">
        <stop offset="0" stop-color="#c9c7b8"/>
        <stop offset=".35" stop-color="#8d9a5c"/>
        <stop offset=".6" stop-color="#c9b88a"/>
        <stop offset="1" stop-color="#2f4a1e"/>
      </linearGradient>
      <linearGradient id="whiteSweep" x1="0" y1="0" x2="1" y2="1">
        <stop offset="0" stop-color="#ffffff"/>
        <stop offset="1" stop-color="#e6e8e7"/>
      </linearGradient>
    </defs>
    <rect width="531" height="400" fill="var(--forest)"/>
    <rect width="531" height="330" fill="#2a5a36" opacity=".35" role="img" aria-label="Faint photo of old Tuscan stone buildings tinted green"/>
    <path d="M0 338 C120 350 240 340 330 310 C410 285 480 290 531 320 L531 683 L0 683Z" fill="url(#whiteSweep)"/>
    <circle cx="176" cy="336" r="143" fill="var(--sand)"/>
    <circle cx="176" cy="330" r="130" fill="url(#hills)" role="img" aria-label="Photo of a Tuscan villa among cypress trees with rolling hills behind"/>
  </svg>

  <h2 class="abs heading-white exp-title--back">What You<br>Will Experience</h2>
  <ul class="abs ticks ticks--back">
    <li><svg width="10" height="10" viewBox="0 0 10 10"><circle cx="5" cy="5" r="4.3" fill="none" stroke="currentColor" stroke-width=".9"/><path d="M3 5.1l1.4 1.4L7 3.8" fill="none" stroke="currentColor" stroke-width=".9"/></svg>4 nights luxury accommodation</li>
    <li><svg width="10" height="10" viewBox="0 0 10 10"><circle cx="5" cy="5" r="4.3" fill="none" stroke="currentColor" stroke-width=".9"/><path d="M3 5.1l1.4 1.4L7 3.8" fill="none" stroke="currentColor" stroke-width=".9"/></svg>All practices, workshops, and guidance</li>
    <li><svg width="10" height="10" viewBox="0 0 10 10"><circle cx="5" cy="5" r="4.3" fill="none" stroke="currentColor" stroke-width=".9"/><path d="M3 5.1l1.4 1.4L7 3.8" fill="none" stroke="currentColor" stroke-width=".9"/></svg>Plant-based meals</li>
    <li><svg width="10" height="10" viewBox="0 0 10 10"><circle cx="5" cy="5" r="4.3" fill="none" stroke="currentColor" stroke-width=".9"/><path d="M3 5.1l1.4 1.4L7 3.8" fill="none" stroke="currentColor" stroke-width=".9"/></svg>Energy &amp; Reiki sessions</li>
    <li><svg width="10" height="10" viewBox="0 0 10 10"><circle cx="5" cy="5" r="4.3" fill="none" stroke="currentColor" stroke-width=".9"/><path d="M3 5.1l1.4 1.4L7 3.8" fill="none" stroke="currentColor" stroke-width=".9"/></svg>Craftwork materials</li>
    <li><svg width="10" height="10" viewBox="0 0 10 10"><circle cx="5" cy="5" r="4.3" fill="none" stroke="currentColor" stroke-width=".9"/><path d="M3 5.1l1.4 1.4L7 3.8" fill="none" stroke="currentColor" stroke-width=".9"/></svg>Forest bathing experience</li>
  </ul>

  <div class="abs name-mark--back" style="top:380px"><span class="dot"></span>THE LANTERN<br>CIRCLE</div>

  <div class="abs pricing">
    <h3 class="sec-title">Pricing</h3>
    <p class="sec-text">Pricing varies by room selection. Full pricing sheet available upon request.</p>
  </div>
  <div class="abs vdots" style="left:245px;top:500px;height:70px"></div>
  <div class="abs reserve">
    <h3 class="sec-title">Reserve Your Place</h3>
    <p class="sec-text">Limited to 5–8 participants. A brief call ensures the retreat aligns with your intentions.</p>
  </div>
  <div class="abs rule"></div>

  <div class="abs contact--back">
    <p class="phone">+41 79 555 01 28</p>
    <p class="web">hello@lanterncircle-retreats.com</p>
    <p class="web">www.LanternCircle-Retreats.com</p>
  </div>
  <div class="abs vdots" style="left:244px;top:596px;height:58px"></div>
  <span class="abs quote-badge">“</span>
  <p class="abs closing">Step into your essence…<br>and emerge transformed</p>
</section>

</body>
</html>
```